DOUBLE SIDED BROCHURE NEEDED TO PROMOTE DOCTOR

I need a double sided DL size (99mm x 210mm) brochure, promoting a doctor seeing patients in a new area.

I want something professional. I have included the relevant information. I would also like the Dr's picture somwhere in the brochure, with a professional background. I wish to print these tomorrow, so i will pick a winner within 14 hours of posting this ad.

I have included an example of a brochures design that I recently saw, and its definietly a good starting point.

Medical

```html
<!DOCTYPE html>
<html lang="en">
<head>
<meta charset="utf-8">
<title>Surgeon Referral Brochure – DL Double Sided</title>
<link rel="stylesheet" href="https://fonts.googleapis.com/css2?family=Arimo:wght@400;700&display=swap">
<style>
  :root {
    --backdrop: #d9d4cc;
    --sky: #6f9fbb;
    --teal: #1f8a8e;
    --mist: #e7ece9;
    --ink-light: #ffffff;
    --ink-teal: #1f8a8e;
    --silver-a: #c9d6da;
    --silver-b: #9fb3b8;
    --photo-a: #b9d4e4;
    --photo-b: #3a3f48;
  }
  * { box-sizing: border-box; margin: 0; padding: 0; }
  html, body { width: 1200px; height: 960px; overflow: hidden; }
  body {
    background: var(--backdrop);
    font-family: "Arimo", Arial, sans-serif;
    font-weight: 700;
    position: relative;
  }
  .panel {
    position: absolute;
    top: 60px;
    width: 396px;
    height: 840px;
    overflow: hidden;
    box-shadow: 0 6px 18px rgba(0,0,0,.25);
  }
  .panel--back { left: 180px; }
  .panel--front { left: 624px; }
  .panel__bg { position: absolute; inset: 0; }
  .copy { position: absolute; color: var(--ink-light); line-height: 1.22; z-index: 2; }
  .copy ul { list-style: none; }
  .copy li::before { content: "• "; }

  .intro { left: 34px; top: 34px; width: 330px; font-size: 18px; }
  .intro ul { margin-top: 6px; }
  .general { left: 34px; top: 400px; width: 330px; font-size: 18px; }
  .general ul { margin-top: 6px; }
  .referral { left: 34px; top: 690px; width: 230px; font-size: 18px; color: var(--ink-teal); }

  .letter { left: 34px; top: 34px; width: 330px; font-size: 17px; }
  .letter p + p { margin-top: 16px; }
  .clinic { left: 34px; top: 418px; width: 330px; font-size: 18px; }
  .clinic h3 { font-size: 18px; margin-bottom: 14px; }

  .emblem {
    position: absolute;
    border-radius: 40px;
    background: linear-gradient(160deg, var(--silver-a), var(--silver-b));
    opacity: .6;
    z-index: 1;
  }
  .panel--back .emblem { right: 0; top: 590px; width: 90px; height: 230px; }
  .panel--front .emblem { left: 0; top: 640px; width: 100px; height: 190px; }

  .portrait {
    position: absolute;
    right: 0; bottom: 0;
    width: 260px; height: 240px;
    background: linear-gradient(180deg, var(--photo-a) 0%, var(--photo-b) 100%);
  }
</style>
</head>
<body>

  <section class="panel panel--back" aria-label="Brochure back side">
    <svg class="panel__bg" width="396" height="840" viewBox="0 0 396 840" aria-hidden="true">
      <rect width="396" height="840" fill="var(--mist)"/>
      <path d="M0 0 H396 V700 C300 680 120 620 0 590 Z" fill="var(--teal)"/>
      <path d="M0 0 H396 V380 C300 370 120 350 0 345 Z" fill="var(--sky)"/>
    </svg>
    <div class="emblem" role="img" aria-label="Silver winged medical staff emblem decoration"></div>
    <div class="copy intro">
      <p>Dr. Haddad is a highly trained specialised surgeon, in all areas of Endocrine, Breast and General Surgery, Including:</p>
      <ul>
        <li>Thyroid Surgery</li>
        <li>Parathyroid surgery (including minimally invasive parathyroidectomy)</li>
        <li>Breast Cancer</li>
        <li>Benign breast lesions</li>
      </ul>
    </div>
    <div class="copy general">
      <p>All areas of general surgery, such as:</p>
      <ul>
        <li>Gallbladder surgery</li>
        <li>Hernia surgery</li>
        <li>Haemorrhoids</li>
        <li>Carpal Tunnel</li>
        <li>Vasectomy etc etc</li>
      </ul>
    </div>
    <p class="copy referral">Please send all referrals by fax to (08) 6000 4821.</p>
  </section>

  <section class="panel panel--front" aria-label="Brochure front side">
    <svg class="panel__bg" width="396" height="840" viewBox="0 0 396 840" aria-hidden="true">
      <rect width="396" height="840" fill="var(--mist)"/>
      <path d="M0 0 H396 V660 C300 650 120 630 0 620 Z" fill="var(--teal)"/>
      <path d="M0 0 H396 V400 C300 395 120 370 0 340 Z" fill="var(--sky)"/>
    </svg>
    <div class="emblem" role="img" aria-label="Silver winged medical staff emblem decoration"></div>
    <div class="copy letter">
      <p>Dear Doctors,</p>
      <p>We are pleased to announce that Dr. Samir Haddad is now consulting in Bayview, seeing public and private patients.</p>
      <p>Guaranteed appointment within two weeks, with patients having the option of surgery at Coastal Health Campus, Riverside General Hospital or St. Clare Hospital Lakeside.</p>
    </div>
    <div class="copy clinic">
      <h3>Bayview Clinic:</h3>
      <p>42 Harbourline Road<br>Bayview WA 6999.<br>Phone: 1300 000 123</p>
    </div>
    <div class="portrait" role="img" aria-label="Portrait photograph of the surgeon in a dark blazer"></div>
  </section>

</body>
</html>
```